Marlow Realty Real Estate Brokerage Recruiting Flyer

We are a real estate brokerage looking to hire more real estate agents. We need to list everything we have to offer as a company so real estate agents will join our company. this is our company website: www.Marlowrealty.example .

100% COMMISSION NO MONTHLY FEE
$450 Flat Transaction FEE

What We Offer:
24/7 Office Access
Free E & O Insurance for 1st Year
Free Online CE and PLE
Free 1,000 Business Cards
Free Professional Social Media Marketing
Free Printing, Scanning, and Copies
Free Buyer and Seller Presentation Packages
Free Filquay Cloud Based Document Management Access
Access to our Internal Brokerage Forum
Company Profit Sharing!
Private Offices Available to Rent

*Lead Generation Software with over 3,000 Leads
*10 Leads to Start
* Free Personal CRM and Website
*Restrictions and Rules apply

Company Address:
4817 Amberfield Road
Suite 512
Fairfax, VA 22194
Phone: 703-555-0147
email: info@marlowrealty.example

Target Market(s)

Real Estate Agents

Industry/Entity Type

Real Estate

Colors
0555a3
ffffff

Requirements
Must have
• 100% COMMISSION NO MONTHLY FEE
$450 Flat Transaction FEE

What We Offer:
24/7 Office Access
Free Online CE and PLE
Free 1,000 Business Cards
Company Profit Sharing!

*10 Leads to Start

Company Address:
4817 Amberfield Road
Suite 512
Fairfax, VA 22194
Phone: 703-555-0147

```html
<!DOCTYPE html>
<html lang="en">
<head>
<meta charset="utf-8">
<title>Marlow Realty – Agent Recruiting Flyer</title>
<link rel="stylesheet" href="https://fonts.googleapis.com/css2?family=Anton&family=Montserrat:wght@300;400;500;600;700&display=swap">
<style>
  :root{
    --navy:#0b3a85;
    --navy-deep:#06275e;
    --brand-blue:#0555a3;
    --ink:#222226;
    --grey:#a9a9ad;
    --grey-light:#d4d4d8;
    --white:#ffffff;
  }
  *{box-sizing:border-box;margin:0;padding:0}
  html,body{width:745px;height:1200px;overflow:hidden;background:var(--white)}
  body{font-family:"Montserrat",Arial,sans-serif;color:var(--ink)}
  .flyer{position:relative;width:745px;height:1200px;overflow:hidden;background:var(--white)}

  /* header */
  .brand{position:absolute;left:30px;top:58px;display:flex;align-items:center;gap:10px}
  .brand-mark{width:34px;height:34px;background:var(--navy)}
  .brand-name{font-weight:600;font-size:20px;color:var(--navy);white-space:nowrap}
  .header-divider{position:absolute;left:246px;top:40px;width:1px;height:105px;background:var(--grey-light)}
  .headline{position:absolute;left:262px;top:40px;font-family:"Anton",Impact,sans-serif;font-size:33px;letter-spacing:.2px;color:var(--ink);white-space:nowrap;line-height:1.1}
  .fee-line{position:absolute;left:262px;top:94px;display:flex;align-items:center;gap:10px}
  .fee-amount{background:var(--navy);color:var(--white);width:140px;height:44px;display:flex;align-items:center;justify-content:center;font-weight:500;font-size:34px;line-height:1}
  .fee-amount sup{font-size:15px;margin-right:4px;align-self:flex-start;margin-top:6px}
  .fee-label{font-weight:600;font-size:26px;color:var(--navy);white-space:nowrap}

  /* hero */
  .hero-frame{position:absolute;left:0;top:160px;width:745px;height:436px;background:var(--grey);border-top-left-radius:150px}
  .hero-photo{position:absolute;left:0;top:168px;width:745px;height:422px;border-top-left-radius:146px;
    background:radial-gradient(ellipse at 38% 55%,rgba(255,170,110,.45) 0,rgba(255,170,110,0) 22%),
               linear-gradient(100deg,#081a36 0%,#10284f 40%,#3c5680 75%,#5d7398 100%)}
  .hex-row{position:absolute;left:0;top:452px;width:745px;height:225px}

  /* offers */
  .offers-title{position:absolute;left:30px;top:680px;font-weight:700;font-size:29px;color:var(--navy)}
  .offers-title::after{content:"";display:block;width:60px;height:3px;background:var(--grey);margin-top:3px}
  .offer-list{position:absolute;top:735px;list-style:none}
  .offer-list.left{left:30px;width:360px}
  .offer-list.right{left:400px;width:340px}
  .offer-list li{display:flex;align-items:center;gap:12px;min-height:31px;font-size:12.5px;font-weight:500;line-height:1.15}
  .offer-list li + li{margin-top:2px}
  .offer-icon{width:24px;height:24px;flex:none;fill:none;stroke:#55575f;stroke-width:1.4}

  .access-pill{position:absolute;left:255px;top:900px;width:262px;height:56px;border-radius:28px;
    background:linear-gradient(180deg,#2b5cae 0%,var(--navy) 55%,var(--navy-deep) 100%);
    border:2px solid #c9d4e8;box-shadow:0 6px 0 -1px var(--grey);
    display:flex;align-items:center;gap:10px;padding-left:14px;color:var(--white)}
  .access-pill svg{width:28px;height:28px}
  .access-hours{font-weight:300;font-size:30px;letter-spacing:-.5px}
  .access-label{font-weight:500;font-size:16px;margin-left:-6px;white-space:nowrap}

  .perks{position:absolute;left:36px;top:990px;width:440px;display:grid;grid-template-columns:210px 220px;row-gap:14px}
  .perk{display:flex;gap:8px;font-size:13px;font-weight:500;line-height:1.15}
  .perk svg{width:14px;height:14px;flex:none;margin-top:1px;fill:none;stroke:var(--navy);stroke-width:1.6}
  .perks-divider{position:absolute;left:486px;top:985px;width:1px;height:92px;background:var(--grey-light)}
  .address{position:absolute;left:510px;top:985px;font-size:14px;font-weight:700;line-height:1.15;font-style:normal}
  .address h3{font-size:15px;font-weight:700;color:var(--navy);margin-bottom:4px}

  /* footer */
  .footer-shape{position:absolute;left:0;top:1050px;width:745px;height:150px}
  .footer-contact{position:absolute;left:56px;right:20px;top:1160px;height:40px;display:flex;align-items:center;color:var(--white);font-size:12px;white-space:nowrap}
  .footer-contact .call{font-size:11px;letter-spacing:.3px;margin-right:7px}
  .footer-contact .phone{font-weight:700;font-size:15px}
  .footer-contact .sep{width:1px;height:22px;background:var(--white);margin:0 11px;flex:none}
</style>
</head>
<body>
<main class="flyer">

  <header>
    <div class="brand"><span class="brand-mark"></span><span class="brand-name">Marlow Realty</span></div>
    <div class="header-divider"></div>
    <h1 class="headline">100% COMMISSION NO MONTHLY FEE</h1>
    <div class="fee-line">
      <span class="fee-amount"><sup>$</sup>450</span>
      <span class="fee-label">Flat Transaction FEE</span>
    </div>
  </header>

  <div class="hero-frame"></div>
  <div class="hero-photo" role="img" aria-label="Businessman's hand hovering over a tablet with glowing figures of people, city skyscrapers in the background"></div>

  <svg class="hex-row" viewBox="0 0 745 225">
    <defs>
      <linearGradient id="hexA" x1="0" y1="0" x2="1" y2="1"><stop offset="0" stop-color="#e9e6e2"/><stop offset="1" stop-color="#8d7b6a"/></linearGradient>
      <linearGradient id="hexB" x1="0" y1="0" x2="0" y2="1"><stop offset="0" stop-color="#d9d9db"/><stop offset="1" stop-color="#6e6a68"/></linearGradient>
      <linearGradient id="hexC" x1="0" y1="0" x2="1" y2="1"><stop offset="0" stop-color="#c9c3bc"/><stop offset="1" stop-color="#6b5648"/></linearGradient>
    </defs>
    <g stroke="#ffffff" stroke-width="4">
      <polygon role="img" aria-label="Agent meeting a client at a desk with a small house model" fill="url(#hexA)" points="196,4 283,54 283,168 196,218 109,168 109,54"/>
      <polygon role="img" aria-label="Hands sheltering a paper cut-out of a family, car and house" fill="url(#hexB)" points="372,4 459,54 459,168 372,218 285,168 285,54"/>
      <polygon role="img" aria-label="Team joining hands together in a circle" fill="url(#hexC)" points="548,4 635,54 635,168 548,218 461,168 461,54"/>
    </g>
  </svg>

  <h2 class="offers-title">What We Offer</h2>

  <ul class="offer-list left">
    <li><svg class="offer-icon" viewBox="0 0 24 24"><path d="M12 2l8 3v6c0 5-3.5 9-8 11-4.5-2-8-6-8-11V5z"/><path d="M8.5 12l2.5 2.5 4.5-5"/></svg>Free E &amp; O Insurance for 1st Year</li>
    <li><svg class="offer-icon" viewBox="0 0 24 24"><rect x="3" y="4" width="18" height="12" rx="1"/><path d="M8 20h8M12 16v4"/></svg>Free Online CE and PLE</li>
    <li><svg class="offer-icon" viewBox="0 0 24 24"><rect x="2" y="5" width="20" height="14" rx="1"/><path d="M5 9h6M5 12h8M14 9h5v6h-5z"/></svg>Free 1,000 Business Cards</li>
    <li><svg class="offer-icon" viewBox="0 0 24 24"><rect x="2" y="3" width="14" height="10" rx="1"/><rect x="9" y="10" width="13" height="10" rx="1"/><path d="M5 7h8M12 14h7M12 17h5"/></svg>Free Professional Social Media Marketing</li>
    <li><svg class="offer-icon" viewBox="0 0 24 24"><path d="M6 9V3h12v6"/><rect x="2" y="9" width="20" height="8" rx="1"/><path d="M6 14h12v7H6z"/></svg>Free Printing, Scanning, and Copies</li>
  </ul>

  <ul class="offer-list right">
    <li><svg class="offer-icon" viewBox="0 0 24 24"><circle cx="7" cy="6" r="2.5"/><circle cx="17" cy="6" r="2.5"/><path d="M3 21v-7a4 4 0 018 0v7M13 21v-7a4 4 0 018 0v7"/></svg>Free Buyer and Seller Presentation Packages</li>
    <li><svg class="offer-icon" viewBox="0 0 24 24"><path d="M4 2h11l4 4v16H4z"/><path d="M7 9h9M7 13h9M7 17h6"/></svg>Free Filquay Cloud Based Document<br>Management Access</li>
    <li><svg class="offer-icon" viewBox="0 0 24 24"><path d="M3 22V8l6-4v18M9 22V10h8v12M21 22V13h-4"/><path d="M5 10h2M5 14h2M12 14h2M12 18h2"/></svg>Access to our Internal Brokerage Forum</li>
    <li><svg class="offer-icon" viewBox="0 0 24 24"><circle cx="8" cy="15" r="5"/><circle cx="16" cy="7" r="4"/><path d="M8 12v6M16 5v4"/></svg>Company Profit Sharing!</li>
    <li><svg class="offer-icon" viewBox="0 0 24 24"><path d="M4 22V4h16v18"/><path d="M8 8h2M14 8h2M8 12h2M14 12h2M8 16h2M14 16h2M10 22v-3h4v3"/></svg>Private Offices Available to Rent</li>
  </ul>

  <div class="access-pill">
    <svg viewBox="0 0 28 28" fill="none" stroke="#ffffff" stroke-width="1.4"><circle cx="14" cy="14" r="12"/><text x="14" y="17" text-anchor="middle" fill="#ffffff" stroke="none" font-family="Montserrat, Arial, sans-serif" font-size="8" font-weight="600">24/7</text></svg>
    <span class="access-hours">24/7</span><span class="access-label">Office Access</span>
  </div>

  <div class="perks">
    <div class="perk"><svg viewBox="0 0 14 14"><circle cx="7" cy="7" r="6"/><path d="M4 7l2 2 4-4"/></svg>Lead Generation Software<br>with over 3,000 Leads</div>
    <div class="perk"><svg viewBox="0 0 14 14"><circle cx="7" cy="7" r="6"/><path d="M4 7l2 2 4-4"/></svg>Free Personal CRM<br>and Website</div>
    <div class="perk"><svg viewBox="0 0 14 14"><circle cx="7" cy="7" r="6"/><path d="M4 7l2 2 4-4"/></svg>10 Leads to Start</div>
    <div class="perk"><svg viewBox="0 0 14 14"><circle cx="7" cy="7" r="6"/><path d="M4 7l2 2 4-4"/></svg>Restrictions and Rules apply</div>
  </div>
  <div class="perks-divider"></div>
  <address class="address">
    <h3>Company Address</h3>
    4817 Amberfield Road<br>Suite 512<br>Fairfax, VA 22194
  </address>

  <svg class="footer-shape" viewBox="0 0 745 150" aria-hidden="true">
    <path d="M0 104 L600 104 Q720 98 745 22 L745 150 L0 150 Z" fill="var(--grey)"/>
    <path d="M8 150 Q24 110 74 110 L745 110 L745 150 Z" fill="var(--navy)"/>
  </svg>
  <footer class="footer-contact">
    <span class="call">CALL US NOW:</span>
    <span class="phone">703-555-0147</span>
    <span class="sep"></span>
    <span>info@marlowrealty.example</span>
    <span class="sep"></span>
    <span>Licensed in D.C., Maryland, and Virginia</span>
  </footer>

</main>
</body>
</html>
```